Wine Label Design for Marrick Estate

I need a front and back label for a new wine I am making. I am looking for a classic, elegant and serious wine label. I would like the label to be white with blue and black writing. The blue will be the distinction in the label. The color of blue will be unique and catch the eye. The font of the writing will be unique and could also serve as the brand image for Marrick Estate. The label can have a design but should be simple and distinct. I envision the paper quality of the label to textured, high quality and add to the overall image of the label.
The label will be timeless. The price of this wine will be $85.00 a bottle, and the label should match a higher priced wine. This wine is family owned and operated.
The writing on the front and back label will be:

FRONT Label-

Marrick Estate

Howell Mountain

Napa Valley

2022 Cabernet Sauvignon

Back Label-

Cellared and Bottled by Marrick Estate, Angwin, CA 94508

GOVERNMENT WARNING: (1) According to the Surgeon General, women should not drink alcoholic beverages during pregnancy because of the risk of birth defects. (2) Consumption of alcoholic beverages impairs your ability to drive a car or operate machinery, and may cause health problems.

Alc. 14.5% by Vol.

750 ml

Contains Sulfites

```html
<!DOCTYPE html>
<html lang="en">
<head>
<meta charset="utf-8">
<title>Marrick Estate – Cabernet Sauvignon Label</title>
<link rel="stylesheet" href="https://fonts.googleapis.com/css2?family=Playfair+Display:wght@400;500&family=Cormorant+Garamond:ital,wght@0,400;1,400&display=swap">
<style>
  :root {
    --paper: #ffffff;
    --navy: #0d2f63;
    --navy-deep: #141c3f;
    --royal: #1f56a6;
    --ink: #2a2a2e;
    --rule: #9aa3b5;
    --band-text: #f3f5fb;
  }
  html, body {
    margin: 0;
    padding: 0;
    width: 1200px;
    height: 1200px;
    overflow: hidden;
    background: var(--paper);
  }
  .label {
    position: relative;
    width: 1200px;
    height: 1200px;
  }
  .leaf-art {
    position: absolute;
    left: 466px;
    top: 176px;
    width: 273px;
    height: 254px;
  }
  .estate-seal {
    position: absolute;
    left: 521px;
    top: 513px;
    width: 72px;
    height: 72px;
    border-radius: 50%;
    background: radial-gradient(circle at 40% 35%, var(--royal), var(--navy-deep) 75%);
  }
  .estate-name {
    position: absolute;
    right: calc(1200px - 593px);
    top: 600px;
    margin: 0;
    text-align: right;
    font-family: "Playfair Display", serif;
    font-weight: 500;
    font-size: 64px;
    line-height: 61px;
    color: var(--navy);
    letter-spacing: 0;
  }
  .region {
    position: absolute;
    right: calc(1200px - 593px);
    top: 728px;
    margin: 0;
    text-align: right;
    font-family: "Cormorant Garamond", serif;
    font-size: 30px;
    line-height: 37px;
    letter-spacing: 1.5px;
    color: var(--ink);
  }
  .divider {
    position: absolute;
    left: 626px;
    top: 496px;
    width: 1px;
    height: 320px;
    background: var(--rule);
  }
  .vintage-details {
    position: absolute;
    left: 665px;
    top: 606px;
    font-family: "Cormorant Garamond", serif;
    font-style: italic;
    color: var(--navy);
  }
  .vintage {
    margin: 0;
    font-size: 46px;
    line-height: 1;
    letter-spacing: 1px;
  }
  .volume, .alcohol {
    margin: 0;
    font-size: 30px;
    line-height: 45px;
  }
  .volume { margin-top: 12px; }
  .varietal-band {
    position: absolute;
    left: 150px;
    top: 851px;
    width: 901px;
    height: 173px;
    border-radius: 8px;
    background: linear-gradient(90deg,
      var(--navy-deep) 0%,
      var(--royal) 16%,
      #24306a 34%,
      #22285a 50%,
      var(--royal) 72%,
      #1a3a7e 86%,
      var(--navy-deep) 100%);
    display: flex;
    align-items: center;
    justify-content: center;
  }
  .varietal {
    margin: 0;
    font-family: "Cormorant Garamond", serif;
    font-style: italic;
    font-size: 48px;
    letter-spacing: 3px;
    color: var(--band-text);
  }
</style>
</head>
<body>
  <main class="label">
    <svg class="leaf-art" role="img" aria-label="Printed vine leaf illustration in deep and bright blue" viewBox="0 0 273 254">
      <defs>
        <radialGradient id="leafTone" cx="50%" cy="50%" r="55%">
          <stop offset="0%" stop-color="#3a5fb0"/>
          <stop offset="100%" stop-color="#1c2e6e" stop-opacity="0.85"/>
        </radialGradient>
      </defs>
      <ellipse cx="136" cy="127" rx="130" ry="120" fill="url(#leafTone)" opacity="0.55"/>
    </svg>

    <span class="estate-seal" aria-hidden="true"></span>

    <h1 class="estate-name">MARRICK<br>ESTATE</h1>
    <p class="region">Howell Mountain<br>Napa Valley</p>

    <span class="divider" aria-hidden="true"></span>

    <div class="vintage-details">
      <p class="vintage">2022</p>
      <p class="volume">750 ml</p>
      <p class="alcohol">13% Vol.</p>
    </div>

    <div class="varietal-band">
      <p class="varietal">Cabernet Sauvignon</p>
    </div>
  </main>
</body>
</html>
```